BRH

Please see our existing website at www.brightriverhealth.com.au
We want to keep the same content and photos but need a new design as the current one looks too clinical and boring.

```html
<!DOCTYPE html>
<html lang="en">
<head>
<meta charset="utf-8">
<title>Bright River Health</title>
<link href="https://fonts.googleapis.com/css2?family=Raleway:wght@500;600;700;800&family=Lato:wght@400;700&family=Fira+Sans:wght@500&family=Kaushan+Script&display=swap" rel="stylesheet">
<style>
:root{
  --green:#2f8f3c;
  --green-dark:#1f6e2a;
  --green-light:#6cc04a;
  --ink:#222;
  --text:#555;
  --band:#eef2ec;
  --field:#f1f3f0;
  --white:#fff;
  --star:#f2a93b;
}
*{box-sizing:border-box;margin:0;padding:0}
html,body{width:1200px;height:4501px;overflow:hidden;background:var(--white)}
body{font-family:"Lato",sans-serif;color:var(--text);position:relative}
.abs{position:absolute}
.brand-name{font-family:"Raleway",sans-serif;font-weight:800;color:var(--green);letter-spacing:1px;line-height:1.05}
/* header */
.site-header{left:0;top:0;width:1200px;height:117px;background:var(--white)}
.site-header .brand-name{left:73px;top:32px;font-size:22px;width:230px}
.nav{left:0;top:55px;font-family:"Lato",sans-serif;font-size:13px;color:var(--ink)}
.nav span{position:absolute;white-space:nowrap;text-transform:uppercase}
.nav .active{color:var(--green)}
/* hero */
.hero{left:0;top:117px;width:1200px;height:660px;background:var(--green);overflow:hidden}
.hero-photo{position:absolute;left:455px;top:0;width:745px;height:660px;background:linear-gradient(90deg,var(--green) 0%,#5d7f5a 22%,#6a6f66 55%,#3c4450 100%)}
.hero-copy{position:absolute;left:72px;top:185px;color:var(--white)}
.hero-copy h1{font-family:"Raleway",sans-serif;font-weight:600;font-size:34px;line-height:41px}
.hero-copy .sub{font-family:"Raleway",sans-serif;font-weight:500;font-size:25px;margin-top:4px}
.hero-copy .script{font-family:"Kaushan Script",cursive;font-size:24px;margin-top:12px}
.btn-dark{position:absolute;left:72px;top:372px;width:160px;height:37px;border-radius:19px;background:var(--ink);color:var(--white);font-size:12px;display:flex;align-items:center;justify-content:center;letter-spacing:.5px}
.dots{position:absolute;left:15px;top:252px}
.dots i{display:block;width:7px;height:7px;border-radius:50%;background:var(--white);margin-bottom:13px}
.dots i.on{background:var(--ink);box-shadow:0 0 0 2px var(--white)}
.hero-wave{left:0;top:660px;width:1200px;height:120px}
/* section titles */
.section-title{font-family:"Raleway",sans-serif;font-weight:700;color:var(--ink);font-size:32px;text-align:center;width:1200px;left:0}
/* about */
.about-rule{left:564px;top:849px;width:70px;height:3px;background:var(--green)}
.about-photo{left:148px;top:838px;width:420px;height:420px;border-radius:50%;background:radial-gradient(circle at 45% 40%,#8a9a8a,#3d5a3f 60%,#2b3a2e)}
.about-copy{left:622px;top:886px;width:470px}
.about-copy h3{font-family:"Fira Sans",sans-serif;font-weight:500;color:var(--green);font-size:20px;line-height:22px}
.about-copy p{font-size:12.5px;line-height:22px;color:#444;margin-top:18px}
.about-copy .mission{font-family:"Fira Sans",sans-serif;color:var(--green);font-size:16px;margin-top:22px}
.btn-green{position:absolute;height:38px;border-radius:19px;background:var(--green);color:var(--white);font-size:13px;display:flex;align-items:center;justify-content:center}
/* services */
.services{left:0;top:1336px;width:1200px;height:993px;background:var(--band)}
.card{position:absolute;width:248px}
.card .photo{width:248px;height:219px;border-radius:12px}
.card h4{font-family:"Raleway",sans-serif;font-weight:700;color:var(--ink);font-size:16px;line-height:21px;margin:20px 0 0 15px;text-transform:uppercase}
.card p{font-size:12px;line-height:22px;color:#555;margin:8px 10px 0 15px;height:66px}
.read-more{display:flex;align-items:center;gap:6px;color:var(--green);font-size:12.5px;margin-left:15px}
.read-more svg{width:15px;height:15px}
/* resources */
.res{position:absolute;width:330px;text-align:center}
.res .photo{width:330px;height:283px;border-radius:12px}
.res h4{font-family:"Raleway",sans-serif;font-weight:700;color:var(--ink);font-size:16px;line-height:21px;margin-top:40px;height:42px}
.res p{font-size:12px;line-height:22px;color:#555;margin:14px 20px 0;height:66px}
.res .read-more{justify-content:center;margin:16px 0 0}
/* testimonials */
.testi{position:absolute;width:304px;height:304px;border-radius:50%;background:var(--band);text-align:center;padding-top:103px}
.quote{position:absolute;left:-24px;top:-1px;width:62px;height:62px;border-radius:50%;background:var(--green);border:4px solid var(--white);color:var(--white);font-family:"Raleway",sans-serif;font-weight:800;font-size:34px;line-height:62px}
.testi .name{font-family:"Raleway",sans-serif;font-weight:700;color:var(--ink);font-size:16px}
.testi .role{color:var(--green);font-size:12px;font-weight:700;margin-top:4px}
.testi .quote-text{font-size:11.5px;line-height:14px;color:#555;margin:12px 26px 0}
.stars{color:var(--star);font-size:12px;letter-spacing:3px;margin-top:22px}
/* booking */
.book-title{left:0;top:3624px;width:1200px;text-align:center;font-family:"Raleway",sans-serif;font-weight:700;color:var(--ink);font-size:33px;line-height:41px}
.field{position:absolute;background:var(--field);font-size:12px;color:#666;padding:13px 16px}
.field .chev{position:absolute;right:16px;top:13px}
/* footer */
.footer-wave{left:0;top:4058px;width:1200px;height:80px}
.footer{left:0;top:4136px;width:1200px;height:301px;background:var(--green)}
.footer-brand{left:101px;top:4161px;width:262px;height:290px;background:var(--white);border-radius:6px 6px 0 0;text-align:center}
.footer-brand .brand-name{font-size:22px;margin-top:92px}
.social{display:flex;gap:12px;justify-content:center;margin-top:56px}
.social i{width:32px;height:32px;border-radius:50%;background:var(--green-dark)}
.f-col{position:absolute;color:var(--white);font-size:12px}
.f-col h5{font-family:"Raleway",sans-serif;font-weight:700;font-size:12px;letter-spacing:.5px}
.f-col .bar{width:38px;height:2px;background:var(--white);margin:10px 0 16px}
.f-col li{list-style:none;line-height:17.5px}
.f-col li::before{content:">";margin-right:10px}
.contact-row{display:flex;gap:10px;align-items:flex-start;line-height:22px}
.contact-row svg{width:13px;height:13px;margin-top:5px;flex:none}
.news-input{left:868px;top:4303px;width:257px;height:38px;border-radius:19px;background:var(--white)}
.news-btn{left:868px;top:4345px;width:257px;height:38px;border-radius:19px;background:var(--green-dark);color:var(--white);font-size:12px;display:flex;align-items:center;justify-content:center}
.copyright{left:0;top:4437px;width:1200px;height:64px;text-align:center;font-size:12px;color:#444;line-height:56px}
.copyright b{color:var(--green);font-weight:400}
</style>
</head>
<body>

<header class="abs site-header">
  <div class="abs brand-name">BRIGHT RIVER<br>HEALTH</div>
  <nav class="abs nav">
    <span class="active" style="left:510px">Home</span>
    <span style="left:589px">About Us</span>
    <span style="left:693px">Our Services</span>
    <span style="left:823px">Resources</span>
    <span style="left:940px">Testimonials</span>
    <span style="left:1071px">Contact</span>
  </nav>
</header>

<section class="abs hero">
  <div class="hero-photo" role="img" aria-label="Trainer guiding a client through a floor exercise in the gym"></div>
  <div class="dots"><i></i><i class="on"></i><i></i></div>
  <div class="hero-copy">
    <h1>Reduce Pain.<br>Improve Core Strength.</h1>
    <div class="sub">Increase Mobility and Movement</div>
    <div class="script">Feel Fitter, Happier, Healthier.</div>
  </div>
  <div class="btn-dark">READ MORE</div>
</section>
<svg class="abs hero-wave" viewBox="0 0 1200 120" preserveAspectRatio="none">
  <path d="M0 0 L1200 0 L1200 70 C900 40 520 20 0 62 Z" fill="var(--green)"/>
  <path d="M0 62 C520 20 900 40 1200 70 L1200 120 L0 120 Z" fill="var(--white)"/>
  <path d="M0 66 C420 28 720 24 1000 50" stroke="var(--ink)" stroke-width="8" fill="none"/>
  <path d="M820 40 C980 48 1100 58 1200 68" stroke="var(--green)" stroke-width="8" fill="none"/>
</svg>

<h2 class="abs section-title" style="top:796px">ABOUT US</h2>
<div class="abs about-rule"></div>
<div class="abs about-photo" role="img" aria-label="Smiling trainer in team uniform holding a tablet"></div>
<div class="abs about-copy">
  <h3>Specialised in injury free functional training with specialised CoreFlex Machines</h3>
  <p>Let's paint the picture. You want to overcome existing pain or back injury, but traditional exercises make it worse. Or perhaps you want to feel fitter and more flexible, but high intensity, sweaty gym classes with the risk of injury just aren't your thing.</p>
  <p>At the Bright River Health our specialist trainers, small group sessions, and top-of-the-range CoreFlex machines mean you can build strength and mobility while preventing future pain and injury.</p>
  <div class="mission">Our Mission + Our Philosophy = Real Results!</div>
</div>
<div class="btn-green" style="left:618px;top:1188px;width:154px">Read More</div>

<section class="abs services">
  <h2 class="abs section-title" style="top:50px">OUR SERVICES</h2>
  <div class="card" style="left:75px;top:124px">
    <div class="photo" role="img" aria-label="Trainer assisting a client on a strength machine" style="background:linear-gradient(135deg,#7d8a80,#2f3a33)"></div>
    <h4>Our CoreFlex Machines</h4>
    <p>CoreFlex machines are not like normal pieces of equipment you'd find in traditional gyms...</p>
    <div class="read-more">Read More <svg viewBox="0 0 16 16"><circle cx="8" cy="8" r="8" fill="var(--green)"/><path d="M6.5 4.5 10 8l-3.5 3.5" stroke="#fff" stroke-width="1.8" fill="none"/></svg></div>
  </div>
  <div class="card" style="left:342px;top:124px">
    <div class="photo" role="img" aria-label="Body composition scanner screen" style="background:linear-gradient(135deg,#3a3d42,#101214)"></div>
    <h4>Vitalscan 360</h4>
    <p>The Vitalscan 360 Body Composition Analyser is like a traditional BMI machine but on steroids...</p>
    <div class="read-more">Read More <svg viewBox="0 0 16 16"><circle cx="8" cy="8" r="8" fill="var(--green)"/><path d="M6.5 4.5 10 8l-3.5 3.5" stroke="#fff" stroke-width="1.8" fill="none"/></svg></div>
  </div>
  <div class="card" style="left:610px;top:124px">
    <div class="photo" role="img" aria-label="Woman doing a kettlebell squat" style="background:linear-gradient(135deg,#6f6a66,#2c3a4a)"></div>
    <h4>Functional Fitness</h4>
    <p>First and foremost, functional fitness exercises can be done by anyone ...</p>
    <div class="read-more">Read More <svg viewBox="0 0 16 16"><circle cx="8" cy="8" r="8" fill="var(--green)"/><path d="M6.5 4.5 10 8l-3.5 3.5" stroke="#fff" stroke-width="1.8" fill="none"/></svg></div>
  </div>
  <div class="card" style="left:875px;top:124px">
    <div class="photo" role="img" aria-label="Person leaping beside a sea cliff at sunset" style="background:linear-gradient(180deg,#b7c2c9,#8a6a4a)"></div>
    <h4>Sedentary Lifestyle</h4>
    <p>Australian Government's Department of Health, sedentary behaviour involves sitting or lying down...</p>
    <div class="read-more">Read More <svg viewBox="0 0 16 16"><circle cx="8" cy="8" r="8" fill="var(--green)"/><path d="M6.5 4.5 10 8l-3.5 3.5" stroke="#fff" stroke-width="1.8" fill="none"/></svg></div>
  </div>

  <div class="card" style="left:75px;top:550px">
    <div class="photo" role="img" aria-label="Trainer coaching a client on a chest machine" style="background:linear-gradient(135deg,#9aa39c,#3b433e)"></div>
    <h4>Personal Training / Functional Training</h4>
    <p style="height:44px">We take a holistic approach to health and wellbeing by coupling...</p>
    <div class="read-more">Read More <svg viewBox="0 0 16 16"><circle cx="8" cy="8" r="8" fill="var(--green)"/><path d="M6.5 4.5 10 8l-3.5 3.5" stroke="#fff" stroke-width="1.8" fill="none"/></svg></div>
  </div>
  <div class="card" style="left:342px;top:550px">
    <div class="photo" role="img" aria-label="Trainer supporting a client during floor exercise" style="background:linear-gradient(135deg,#8e9690,#2a3344)"></div>
    <h4>Personal Training for over 40's</h4>
    <p style="height:44px">We've all heard the expression 'move it or lose it...</p>
    <div class="read-more">Read More <svg viewBox="0 0 16 16"><circle cx="8" cy="8" r="8" fill="var(--green)"/><path d="M6.5 4.5 10 8l-3.5 3.5" stroke="#fff" stroke-width="1.8" fill="none"/></svg></div>
  </div>
  <div class="card" style="left:610px;top:550px">
    <div class="photo" role="img" aria-label="Happy child jumping in a grassy field" style="background:linear-gradient(180deg,#c9d6a8,#7f8c4a)"></div>
    <h4>Movement Made Fun for Children with ASD</h4>
    <p style="height:44px">Regardless of whether your child has been diagnosed with autism,</p>
    <div class="read-more">Read More <svg viewBox="0 0 16 16"><circle cx="8" cy="8" r="8" fill="var(--green)"/><path d="M6.5 4.5 10 8l-3.5 3.5" stroke="#fff" stroke-width="1.8" fill="none"/></svg></div>
  </div>
  <div class="card" style="left:875px;top:550px">
    <div class="photo" role="img" aria-label="Client lying on a red back extension machine" style="background:linear-gradient(135deg,#d9dcdc,#b23a3a)"></div>
    <h4>Back and Neck Pain</h4>
    <p>Approximately 1 in 6 Australians suffer from back pain each year, and it's one of the leading causes...</p>
    <div class="read-more">Read More <svg viewBox="0 0 16 16"><circle cx="8" cy="8" r="8" fill="var(--green)"/><path d="M6.5 4.5 10 8l-3.5 3.5" stroke="#fff" stroke-width="1.8" fill="none"/></svg></div>
  </div>
</section>

<h2 class="abs section-title" style="top:2403px">RESOURCES</h2>
<div class="res" style="left:75px;top:2491px">
  <div class="photo" role="img" aria-label="Group stretching session on the gym floor" style="background:linear-gradient(135deg,#a8aca8,#3a4458)"></div>
  <h4>THE IMPORTANCE OF<br>STRETCHING</h4>
  <p>A stiff, tight and inflexible body is a one way ticket to poor moods, low energy levels, frequent back and neck pain,...</p>
  <div class="read-more">Read More <svg viewBox="0 0 16 16"><circle cx="8" cy="8" r="8" fill="var(--green)"/><path d="M6.5 4.5 10 8l-3.5 3.5" stroke="#fff" stroke-width="1.8" fill="none"/></svg></div>
</div>
<div class="res" style="left:435px;top:2491px">
  <div class="photo" role="img" aria-label="Office worker at a laptop holding a sore neck" style="background:linear-gradient(135deg,#eeeeee,#9a9a9a)"></div>
  <h4>PAIN AND INJURY MANAGEMENT<br>FOR OFFICE WORKERS</h4>
  <p>If you relate to any of the following, you will most certainly understand the strong relationship between work and back pain:</p>
  <div class="read-more">Read More <svg viewBox="0 0 16 16"><circle cx="8" cy="8" r="8" fill="var(--green)"/><path d="M6.5 4.5 10 8l-3.5 3.5" stroke="#fff" stroke-width="1.8" fill="none"/></svg></div>
</div>
<div class="res" style="left:795px;top:2491px">
  <div class="photo" role="img" aria-label="Client on a red back extension machine with trainer" style="background:linear-gradient(135deg,#dcdedd,#b23a3a)"></div>
  <h4>FREEDOM FROM PAIN</h4>
  <p>CoreFlex equipment has been scientifically designed and uses proven technology that incorporates millions...</p>
  <div class="read-more">Read More <svg viewBox="0 0 16 16"><circle cx="8" cy="8" r="8" fill="var(--green)"/><path d="M6.5 4.5 10 8l-3.5 3.5" stroke="#fff" stroke-width="1.8" fill="none"/></svg></div>
</div>
<div class="btn-green" style="left:519px;top:3027px;width:154px">View &nbsp;More</div>

<h2 class="abs section-title" style="top:3122px">TESTIMONIALS</h2>
<div class="testi" style="left:113px;top:3223px">
  <div class="quote">&ldquo;</div>
  <div class="name">Liam Porter</div>
  <div class="role">Creative Director</div>
  <div class="quote-text">Lorem Ipsum simply dummy text printing and typesetting industry simply dummy a psum is simply dummy</div>
  <div class="stars">★★★★★</div>
</div>
<div class="testi" style="left:454px;top:3223px">
  <div class="quote">&ldquo;</div>
  <div class="name">Sarah Whitfield</div>
  <div class="role">Creative Director</div>
  <div class="quote-text">Lorem Ipsum simply dummy text printing and typesetting industry simply dummy a psum is simply dummy</div>
  <div class="stars">★★★★★</div>
</div>
<div class="testi" style="left:789px;top:3223px">
  <div class="quote">&ldquo;</div>
  <div class="name">Tom Reddan</div>
  <div class="role">Creative Director</div>
  <div class="quote-text">Lorem Ipsum simply dummy text printing and typesetting industry simply dummy a psum is simply dummy</div>
  <div class="stars">★★★★★</div>
</div>

<h2 class="abs book-title">BOOK YOUR COMPLIMENTARY PERSONAL<br>TRAINING SESSION NOW!</h2>
<div class="field" style="left:267px;top:3717px;width:217px;height:40px">Name</div>
<div class="field" style="left:498px;top:3717px;width:216px;height:40px">Phone</div>
<div class="field" style="left:728px;top:3717px;width:217px;height:40px">Email</div>
<div class="field" style="left:267px;top:3773px;width:678px;height:40px">Injury and Rehabilitation<span class="chev">&#8964;</span></div>
<div class="field" style="left:267px;top:3827px;width:678px;height:135px">Message</div>
<div class="btn-green" style="left:519px;top:3990px;width:154px;height:37px">Submit</div>

<svg class="abs footer-wave" viewBox="0 0 1200 80" preserveAspectRatio="none">
  <path d="M0 80 L0 40 C300 60 800 40 1200 0 L1200 80 Z" fill="var(--green)"/>
  <path d="M380 58 C700 54 950 34 1200 4" stroke="var(--ink)" stroke-width="6" fill="none"/>
</svg>
<footer class="abs footer"></footer>
<div class="abs footer-brand">
  <div class="brand-name">BRIGHT RIVER<br>HEALTH</div>
  <div class="social"><i></i><i></i><i></i><i></i></div>
</div>
<div class="f-col" style="left:424px;top:4218px">
  <h5>QUICK LINKS</h5><div class="bar"></div>
  <ul><li>Home</li><li>About Us</li><li>Our Services</li><li>Resources</li><li>Testimonials</li><li>Contact Us</li></ul>
</div>
<div class="f-col" style="left:611px;top:4218px">
  <h5>QUICK CONTACT</h5><div class="bar"></div>
  <div class="contact-row"><svg viewBox="0 0 16 16"><path d="M3 1.5 6 1l1.5 4-2 1.2a9 9 0 0 0 4.3 4.3L11 8.5l4 1.5-.5 3c-7 .5-12-5-11.5-11.5z" fill="#fff"/></svg>07 5550 1234</div>
  <div class="contact-row"><svg viewBox="0 0 16 16"><rect x="1" y="3" width="14" height="10" fill="#fff"/><path d="M1 3l7 6 7-6" stroke="var(--green)" stroke-width="1.4" fill="none"/></svg>info@brightriverhealth.com.au</div>
  <div class="contact-row" style="margin-top:22px"><svg viewBox="0 0 16 16"><path d="M8 1a5 5 0 0 0-5 5c0 4 5 9 5 9s5-5 5-9a5 5 0 0 0-5-5z" fill="#fff"/><circle cx="8" cy="6" r="2" fill="var(--green)"/></svg>5/120 Riverbend Parade<br>Riverside QLD 4000</div>
</div>
<div class="f-col" style="left:868px;top:4232px">
  <h5>NEWSLETTER</h5><div class="bar"></div>
</div>
<div class="abs news-input"></div>
<div class="abs news-btn">SUBSCRIBE</div>
<div class="abs copyright">Copyright © 2021 <b>Bright River Health</b>, All Rights Reserved.</div>

</body>
</html>
```